Business Card for Brevikpartners

Need to design a business card with attached logo

Target Market(s)

I'm a financial/Investment adviser so card must be professional

Industry/Entity Type

Business

Font styles to use
Serif
Sans Serif

Requirements
Must have
• Would like in include the GOLD version of my logo if possible

Teodor Brevik
President

Address is
4278 Pemberly Ave
San Ramon, Ca. 94617

Phone
510-647-3920
Fax
925-413-7782

Email
teodor@brevikpartners.example

I also need the following tag line at the bottom of card:

Investment Advisor Representative of and Securities offered
through Harwick Capital Brokerage, LLC Member NTVQA, OLBR
and Registered Investment Advisor.

Nice to have
• Split color in order to incorporate GOLD LOGO
Should not have

```html
<!DOCTYPE html>
<html lang="en">
<head>
<meta charset="utf-8">
<title>Brevik Partners — Business Card</title>
<link rel="stylesheet" href="https://fonts.googleapis.com/css2?family=Cinzel:wght@500;600;700&family=Questrial&family=Ubuntu:wght@400&display=swap">
<style>
  :root {
    --backdrop: #4a2c1a;
    --navy-deep: #0d0847;
    --navy-mid: #19125f;
    --navy-glow: #2f3188;
    --gold: #d8b55e;
    --gold-light: #f3dc92;
    --gold-dark: #a9822f;
    --text-light: #f2f1fa;
    --text-soft: #d9d6ee;
  }
  * { margin: 0; padding: 0; box-sizing: border-box; }
  html, body {
    width: 1200px;
    height: 1000px;
    overflow: hidden;
    background: var(--backdrop);
  }
  .business-card {
    position: absolute;
    left: 217px;
    top: 236px;
    width: 766px;
    height: 509px;
    background: radial-gradient(ellipse 420px 330px at 500px 250px, var(--navy-glow) 0%, var(--navy-mid) 55%, var(--navy-deep) 100%);
    overflow: hidden;
  }
  .compliance-note {
    position: absolute;
    left: 153px;
    top: 28px;
    font-family: "Ubuntu", sans-serif;
    font-size: 14.5px;
    line-height: 20px;
    color: var(--text-light);
  }
  .brand-block {
    position: absolute;
    left: 30px;
    top: 200px;
    width: 240px;
    text-align: center;
  }
  .brand-mark {
    display: block;
    margin: 0 auto 16px;
  }
  .brand-name {
    font-family: "Cinzel", serif;
    font-weight: 600;
    font-size: 24px;
    color: var(--gold);
    white-space: nowrap;
  }
  .divider {
    position: absolute;
    left: 285px;
    top: 152px;
    width: 2px;
    height: 260px;
    background: var(--gold-dark);
  }
  .person {
    position: absolute;
    left: 320px;
    top: 158px;
    width: 366px;
    text-align: center;
  }
  .person-name {
    font-family: "Cinzel", serif;
    font-weight: 700;
    font-size: 29px;
    letter-spacing: 0.5px;
    background: linear-gradient(180deg, var(--gold-light) 0%, var(--gold) 50%, var(--gold-dark) 100%);
    -webkit-background-clip: text;
    background-clip: text;
    color: transparent;
  }
  .person-title {
    font-family: "Cinzel", serif;
    font-weight: 500;
    font-size: 16px;
    letter-spacing: 1px;
    color: var(--text-soft);
    margin-top: 2px;
    margin-left: -10px;
  }
  .contact-list {
    position: absolute;
    left: 339px;
    top: 274px;
    font-family: "Questrial", sans-serif;
    font-size: 19px;
    line-height: 25px;
    color: var(--text-light);
    display: grid;
    grid-template-columns: 95px auto;
  }
  .contact-label { white-space: nowrap; }
  .contact-value { white-space: nowrap; }
</style>
</head>
<body>
  <main class="business-card">
    <p class="compliance-note">
      Investment Advisor Representative of and Securities offered<br>
      through Harwick Capital Brokerage, LLC Member NTVQA, OLBR<br>
      and Registered Investment Advisor
    </p>

    <div class="brand-block">
      <svg class="brand-mark" width="80" height="80" viewBox="0 0 80 80" aria-hidden="true">
        <circle cx="40" cy="40" r="36" fill="none" stroke="var(--gold)" stroke-width="5"/>
      </svg>
      <div class="brand-name">Brevik Partners</div>
    </div>

    <div class="divider"></div>

    <section class="person">
      <h1 class="person-name">TEODOR BREVIK</h1>
      <p class="person-title">PRESIDENT</p>
    </section>

    <dl class="contact-list">
      <dt class="contact-label">Address :</dt>
      <dd class="contact-value">4278 Pemberly Ave</dd>
      <dt class="contact-label"></dt>
      <dd class="contact-value">San Ramon, Ca. 94617</dd>
      <dt class="contact-label">Phone:</dt>
      <dd class="contact-value">510-647-3920</dd>
      <dt class="contact-label">Fax:</dt>
      <dd class="contact-value">925-413-7782</dd>
      <dt class="contact-label">Email:</dt>
      <dd class="contact-value">teodor@brevikpartners.example</dd>
    </dl>
  </main>
</body>
</html>
```